Surgical Procedure Room Letterhead

PLEASE DO NOT MAKE YOUR LETTERHEAD SIMILAR TO THE ONE I AM INCLUDING IN MY UPLOADS

Hello! I need my logo used to make a very clean, professional, simple letterhead that has all the pertinent information in it:
Location: 4182 NW 38th Lane, Suite 500
Tamarac, FL 33967
Phone: 954-218-4650
Fax: 800-642-9082

Can you please put this all on a word document that is easily editable? I will include my practice letterhead as an example ONLY of how easy it should be to write below the letterhead. Please don't make this letterhead the same as the one I am including in this example. They are two separate businesses.

Target Market(s)

Insurance companies

Industry/Entity Type

medical

Requirements
Must have
• classiness, elegance, simplicity
Should not have
• Please don't make your letterhead the same as the one that I included in my uploads

```html
<!DOCTYPE html>
<html lang="en">
<head>
<meta charset="utf-8">
<title>Meridian Suites Letterhead</title>
<link rel="stylesheet" href="https://fonts.googleapis.com/css2?family=Montserrat:wght@400&family=Work+Sans:wght@400;500&display=swap">
<style>
  :root {
    --backdrop: #e4e7eb;
    --paper: #ffffff;
    --navy: #1f3a68;
    --gold: #c9a43a;
    --text-grey: #7d7d7d;
    --faint-circle: #efe6cc;
  }
  * { margin: 0; padding: 0; box-sizing: border-box; }
  html, body {
    width: 1200px; height: 900px; overflow: hidden;
    background: var(--backdrop);
  }
  .letterhead {
    position: absolute; left: 296px; top: 20px;
    width: 608px; height: 860px;
    background: var(--paper);
    box-shadow: 0 4px 18px rgba(0,0,0,0.12);
    font-family: "Montserrat", sans-serif;
    color: var(--text-grey);
  }
  .brand {
    position: absolute; left: 42px; top: 58px;
    display: flex; align-items: center; gap: 10px;
  }
  .brand-mark {
    width: 22px; height: 22px; border-radius: 50%;
    background: var(--gold);
  }
  .brand-name {
    font-family: "Work Sans", sans-serif; font-weight: 500;
    font-size: 22px; letter-spacing: 0.5px; color: var(--navy);
  }
  .contact {
    position: absolute; left: 421px; top: 44px;
    font-size: 10.5px; line-height: 15.5px; list-style: none;
  }
  .contact li { display: flex; align-items: center; gap: 4px; }
  .contact svg { width: 9px; height: 9px; fill: var(--navy); flex: none; }
  .address {
    position: absolute; left: 421px; top: 118px;
    font-size: 10.5px; line-height: 15.5px; font-style: normal;
  }
  .greeting {
    position: absolute; left: 42px; top: 228px;
    font-family: "Work Sans", sans-serif; font-size: 18px;
  }
  .body-copy {
    position: absolute; left: 42px; top: 284px; width: 526px;
    font-size: 11px; line-height: 15.8px;
  }
  .body-copy p { margin-bottom: 18px; }
  .body-copy p.spaced { margin-top: 26px; }
  .signature {
    position: absolute; left: 42px; top: 620px;
    width: 184px; height: 26px;
    background: linear-gradient(90deg, #f1f2f5, #e6e8ec);
  }
  .signer {
    position: absolute; left: 43px; top: 662px;
    font-family: "Work Sans", sans-serif; font-size: 19px; color: var(--navy);
  }
  .seal {
    position: absolute; left: 420px; top: 640px;
    width: 150px; height: 180px;
  }
</style>
</head>
<body>
<main class="letterhead">
  <header>
    <div class="brand">
      <span class="brand-mark"></span>
      <span class="brand-name">Meridian Suites</span>
    </div>
    <ul class="contact">
      <li><svg viewBox="0 0 10 10"><path d="M2 0.5 L4 2.8 L3 4 Q4.5 6 6 7 L7.2 6 L9.5 8 L8 9.7 Q3 9 0.3 2 Z"/></svg>954-218-4650</li>
      <li><svg viewBox="0 0 10 10"><path d="M2.5 0.5h5v2.5h-5zM0.5 3.5h9v4h-1.5v-1.5h-6v1.5h-1.5zM2.5 6.5h5v3h-5z"/></svg>800-642-9082</li>
      <li><svg viewBox="0 0 10 10"><path d="M0.5 1.5h9v7h-9zM1.5 2.5v0.4l3.5 2.6 3.5-2.6v-0.4zM1.5 4.1v3.4h7v-3.4l-3.5 2.6z" fill-rule="evenodd"/></svg>info@meridiansuites.com</li>
      <li><svg viewBox="0 0 10 10"><circle cx="5" cy="5" r="4.3" fill="none" stroke="#1f3a68" stroke-width="0.9"/><ellipse cx="5" cy="5" rx="1.8" ry="4.3" fill="none" stroke="#1f3a68" stroke-width="0.8"/><path d="M0.7 5h8.6" stroke="#1f3a68" stroke-width="0.8"/></svg>www.meridiansuites.com</li>
    </ul>
    <address class="address">4182 NW 38th Lane, Suite 500<br>Tamarac, FL 33967</address>
  </header>

  <p class="greeting">Dear sir,</p>

  <section class="body-copy">
    <p>Lorem ipsum dolor sit amet, an vel recteque dissentiet, detracto albucius platonem ex vel, eros repudiandae cu. Atqui aliquando nec an, unum graece adolescens vel ad. Id odio scae has, iudico euismod atomorum ius ea, cum ea honestatis quaerendum theophrastus. Mea honestatis quaerendum theophrastus. Mea</p>
    <p>Lorem ipsum dolor sit amet, an vel recteque dissentiet, detracto albucius platonem ex vel, eros repudiandae cu. Atqui aliquando nec an, unum graece adolescens vel ad. Id odio scae has, iudico euismod atomorum ius ea, cum ea honestatis quaerendum theophrastus. Mea doming repudiandae ex, cu cum civibus assentior posidonium. Quo etiam pertinax ex, te eros repudiandae cu. Atqui aliquando nec an, unum graece adolescens vel ad. Id odio scae honestatis quaerendum theophrastus. Mea</p>
    <p>eros repudiandae cu. Atqui aliquando nec an, unum graece adolescens vel ad. Id odio scae honestatis quaerendum theophrastus. Mea posidonium. Quo etiam pertinax ex, te<br>etiam pertinax ex, te</p>
    <p class="spaced">eros repudiandae cu. Atqui aliquando nec an, unum graece adolescens vel ad. Id odio scae honestatis quaerendum theophrastus. Mea posidonium. Quo etiam pertinax ex, te<br>etiam pertinax ex, te</p>
  </section>

  <div class="signature" role="img" aria-label="Handwritten signature of Daniel Harper"></div>
  <p class="signer">Daniel Harper</p>

  <svg class="seal" viewBox="0 0 150 180" aria-hidden="true">
    <circle cx="75" cy="90" r="72" fill="none" stroke="var(--faint-circle)" stroke-width="6"/>
  </svg>
</main>
</body>
</html>
```